Morvena Designs - Online Shoe Shop

Morvena is an online shoes and bags shop. We sell Imported Genuine Leather shoes and bags our market is LSM 8-10. We mainly sell women shoes and bags and we will also be introducing men’s shoes and belts.
I would like a website design and development that is responsive, clean, elegant and easy to use. Where customers can make a purchase online.
Have CATEGORIES in SHOE STYLE (i.e. Heels, Sandals, Pumps, Mules, Boots, Sneaker, Flats, etc) and PRICE RANGE should be in South African Rands currency, COLOUR, SIZE.
For shoe images we should be able to add videos as well.
Header and Footer Menu should have the basic menu list. Header Menu (New Arrivals, Preorder, Women’s Collection, Men’s Collection, Summer 2020 Collection, Winter 2020 Collection, Bags, Accessories, Sale, etc
Auto display when the item is SOLD OUT. Add an option for a user to get notification on when the item is back in stock.
Icons to show when shoes are on sale and Show was and now price.
Users to be able to review and rate the items.
Discount codes for new email subscribers.
Consumers should be able to pay using different options, Credit card, CoinLane, EFT, etc
Add an option for discount coupons at checkout.
After placing and order they should receive an email with order receipt.
Site should have a shipping and tracking option. International shipping such as QRT and SWIFTBOX. For local shipping in South Africa please add Redtrail Couriers and Ulvoro Couriers.
Backend: Backend should be easy to add more categories, items and changing header banners, adding sale alerts. To get notification when the stock is low and sold out. Get notification when an order is placed online so to prepare packing for shipping.
Can we make sure that the SEO is in place and bare in mind all searchly rules to avoid being penalized.
Target Market(s)
Women from age 25-65
LSM 8-10
Entire South Africa and neighboring countries
Industry/Entity Type
Shoe Store
Coding
Coded - Design and coding required
Number of Pages Required
5+ page
Requirements
Must have
- Responsive
Clean
Modern
Shopping cart
Shipping options integration
Newsletter subscription
Social media icons
Nice to have
- The business colors are Gold and White or Gold and Black

```html
<!DOCTYPE html>
<html lang="en">
<head>
<meta charset="utf-8">
<title>Morvena – Shoes &amp; Bags</title>
<link href="https://fonts.googleapis.com/css2?family=Libre+Baskerville:ital,wght@0,400;0,700;1,400&family=Roboto:wght@300;400;500;700&display=swap" rel="stylesheet">
<style>
:root{
  --gold:#e8b512;
  --dark:#2b2b2b;
  --ink:#333;
  --muted:#8a8a8a;
  --line:#e6e6e6;
  --page:#f8f8f8;
  --white:#fff;
}
*{margin:0;padding:0;box-sizing:border-box}
html,body{width:1200px;height:3743px;overflow:hidden}
body{position:relative;background:var(--page);font-family:'Roboto',sans-serif;color:var(--ink)}
.abs{position:absolute}
.serif{font-family:'Libre Baskerville',serif}

/* top bar */
.topbar{left:0;top:0;width:1200px;height:45px;background:var(--dark);color:#fff;font-size:10px;font-weight:500}
.topbar .social{left:163px;top:17px;display:flex;gap:10px}
.dot{width:10px;height:10px;border-radius:50%;background:#fff;opacity:.85}
.topbar .info{left:0;width:1200px;top:16px;text-align:center;letter-spacing:.2px}
.topbar .info span{margin:0 14px;opacity:.6}
.topbar .tools{left:968px;top:14px;display:flex;gap:14px}

/* header */
.header{left:0;top:45px;width:1200px;height:92px;background:var(--white)}
.logo{left:160px;top:26px;display:flex;align-items:center;gap:8px}
.logo .mark{width:22px;height:22px;background:var(--dark)}
.logo b{font-size:20px;font-weight:700;color:var(--dark)}
.promo{left:363px;top:28px}
.promo p{font-family:'Libre Baskerville',serif;font-style:italic;font-size:13px;color:#444}
.promo p em{color:var(--gold)}
.promo small{display:block;font-size:8px;color:var(--muted);margin-top:5px}
.search{left:761px;top:27px;width:225px;height:37px;border:1px solid var(--line);font-size:11px;color:#777;padding:12px 18px;letter-spacing:.5px}
.search svg{position:absolute;right:16px;top:12px}
.cart{left:1010px;top:31px}
.cart .badge{position:absolute;left:-4px;top:-3px;width:15px;height:15px;border-radius:50%;background:var(--gold);color:#fff;font-size:9px;text-align:center;line-height:15px}

/* nav */
.nav{left:0;top:137px;width:1200px;height:69px;background:var(--white);border-top:1px solid #f0f0f0}
.nav ul{position:absolute;left:177px;width:846px;top:27px;display:flex;justify-content:space-between;list-style:none;font-size:11.5px;color:#222;font-weight:500}
.nav li.active{color:var(--gold);text-decoration:underline}
.nav li i{font-style:normal;font-size:9px;margin-left:6px}

/* hero */
.hero{left:0;top:206px;width:1200px;height:516px;background:linear-gradient(100deg,#8d8d8d 0%,#bdbdbd 30%,#d2d2d2 55%,#c9c9c9 100%)}
.hero .photo{left:130px;top:0;width:520px;height:516px;background:linear-gradient(90deg,#777 0%,#a9a9a9 40%,#d8d8d8 70%,rgba(210,210,210,0) 100%)}
.hero .copy{left:673px;top:160px;color:#222}
.hero .kick{font-size:12.5px;font-weight:300}
.hero h2{font-family:'Libre Baskerville',serif;font-weight:400;font-size:24px;margin-top:18px;letter-spacing:.5px}
.hero h3{font-family:'Libre Baskerville',serif;font-weight:700;font-size:29px;letter-spacing:1px;margin-top:-2px}
.hero .sub{font-size:12.5px;font-weight:300;margin-top:10px}
.btn{display:inline-block;background:var(--dark);color:#fff;font-size:9.5px;font-weight:700;text-align:center;letter-spacing:.3px}
.hero .btn{position:absolute;left:673px;top:314px;width:114px;height:39px;line-height:39px}
.hero .dots{left:571px;top:471px;display:flex;gap:8px}
.hero .dots span{width:14px;height:14px;border-radius:50%;background:#eee;border:2px solid #bbb}
.hero .dots span.on{background:#333}

/* section titles */
.title{left:0;width:1200px;text-align:center;font-family:'Libre Baskerville',serif;font-size:24px;letter-spacing:3px;color:#222}
.title::after{content:"";display:block;width:38px;height:2px;background:var(--gold);margin:14px auto 0}

/* products */
.card{width:202px;text-align:center}
.card .img{height:225px;background:var(--white);position:relative}
.card .stars{margin-top:10px;font-size:12px;color:#777;letter-spacing:2px}
.card .name{font-family:'Libre Baskerville',serif;font-size:13px;color:#444;margin-top:6px}
.card .price{font-size:13px;font-weight:700;color:#222;margin-top:6px}
.tag{position:absolute;right:0;top:0;width:107px;height:45px;background:var(--gold);color:#fff;font-size:11px;font-weight:500;line-height:45px;text-align:center}
.shape{position:absolute;left:50%;top:50%;transform:translate(-50%,-50%)}
.active-card{background:#fff;border:1px solid var(--line)}
.active-card .img{border:1px solid var(--line)}
.tools-v{position:absolute;left:13px;top:12px;display:flex;flex-direction:column;gap:6px}
.tools-v span{width:20px;height:20px;background:var(--dark);display:flex;align-items:center;justify-content:center}
.arrow{position:absolute}
.divider{left:161px;top:1235px;width:878px;height:1px;background:#ececec}

/* collections */
.tile{position:absolute;overflow:hidden}
.tile .panel{position:absolute;background:rgba(255,255,255,.78);text-align:center}
.tile h4{font-size:14px;letter-spacing:2px;font-weight:500;color:#222}
.tile .btn{width:114px;height:39px;line-height:39px;margin-top:14px}
.tile small{display:block;font-size:9.5px;color:#888;margin-top:5px}

/* notify */
.notify{left:842px;top:2219px;font-size:9px;color:#777;display:flex;align-items:center;gap:7px}

/* news */
.news{width:278px;background:var(--white);height:384px}
.news .img{height:150px;position:relative}
.news .date{position:absolute;right:10px;bottom:8px;font-size:15px;font-weight:500;color:#222}
.news .date small{font-size:8px;color:#666;font-weight:400}
.news .meta{display:flex;justify-content:space-between;margin:22px 23px 0;font-size:8.5px;color:#777}
.news .meta b{display:inline-block;width:7px;height:7px;border-radius:50%;background:var(--gold);margin-right:4px;vertical-align:-1px}
.news h5{font-size:14px;font-weight:500;color:#222;margin:10px 23px 0;line-height:21px}
.news p{font-size:8.5px;color:#999;margin:10px 23px 0;line-height:18px}
.news .btn{margin:22px 0 0 23px;width:115px;height:40px;line-height:40px}
.nfy{left:760px;top:2560px;width:254px;text-align:center}
.nfy h4{font-family:'Libre Baskerville',serif;font-weight:400;font-size:20px;letter-spacing:2px;color:#222}
.nfy h4::after{content:"";display:block;width:34px;height:2px;background:var(--gold);margin:12px auto 0}
.nfy small{display:block;font-size:9px;color:#888;margin-top:16px}
.nfy .pn{display:flex;justify-content:center;gap:34px;margin-top:22px;font-size:10px;font-weight:700}
.nfy .pn .next{color:var(--gold)}

/* testimonial */
.avatar{left:563px;top:2878px;width:74px;height:74px;border-radius:50%;background:linear-gradient(135deg,#c9b6a2,#6b5545)}
.quote-mark{left:0;width:1200px;top:2978px;text-align:center;font-family:'Libre Baskerville',serif;font-size:36px;color:var(--gold);line-height:1}
.quote{left:230px;width:740px;top:3023px;text-align:center;font-style:italic;font-size:11.5px;color:#777;line-height:22.5px}
.qline{left:562px;top:3116px;width:76px;height:1px;background:#ddd}
.author{left:0;width:1200px;top:3144px;text-align:center;font-family:'Libre Baskerville',serif;font-size:15px;color:#222}
.author small{font-size:10px;color:#666}

/* footer */
.footer{left:161px;top:3234px;width:878px;height:366px;background:var(--white)}
.fcol{position:absolute;top:40px}
.fcol h6{font-size:17px;font-weight:400;color:#222}
.fcol ul{list-style:none;margin-top:38px;font-size:11px;color:#999}
.fcol li{margin-bottom:12px}
.fcol li::before{content:"•";font-size:8px;margin-right:6px}
.vsep{position:absolute;top:40px;width:1px;height:290px;background:#eee}
.news-l{left:237px;width:363px;text-align:center}
.news-l h6{font-family:'Libre Baskerville',serif;font-weight:700;font-size:24px;letter-spacing:3px}
.news-l p{font-size:11px;color:#666;line-height:18px;margin-top:32px}
.subs{position:relative;margin:40px auto 0;width:233px;height:44px;border:1px solid #e5e5e5;border-radius:22px;text-align:left;padding:15px 18px;font-size:9px;font-style:italic;color:#aaa}
.subs span{position:absolute;right:-1px;top:-1px;width:44px;height:44px;border-radius:50%;background:var(--dark);display:flex;align-items:center;justify-content:center}
.contact p{font-size:11px;color:#666;line-height:18px;margin-top:38px}
.contact p+p{margin-top:12px}

.bottom{left:160px;top:3626px;width:880px;font-size:11px;color:#444;display:flex;justify-content:space-between;align-items:center}
.pay{display:flex;gap:14px;align-items:center}
.pay b{font-size:10px;font-weight:700;color:#3a3a8c}
.bottom .find{display:flex;gap:9px;align-items:center}
.bottom .find .dot{background:#bbb;width:9px;height:9px}
.bnav{left:0;top:3676px;width:1200px;height:67px;background:var(--white)}
.bnav ul{position:absolute;left:177px;width:846px;top:26px;display:flex;justify-content:space-between;list-style:none;font-size:11.5px;font-weight:500;color:#222}
</style>
</head>
<body>

<!-- top bar -->
<div class="abs topbar">
  <div class="abs social" aria-label="Social links"><span class="dot"></span><span class="dot" style="background:var(--gold)"></span><span class="dot"></span></div>
  <div class="abs info">TOLL FREE : (00) 000 111 222<span>|</span>MAIL INFO : info@morvenamail.com</div>
  <div class="abs tools">
    <svg width="14" height="14" viewBox="0 0 14 14" fill="none" stroke="#fff" stroke-width="1.3"><path d="M5 1h7v12H5M1 7h7M6 4l3 3-3 3"/></svg>
    <svg width="14" height="14" viewBox="0 0 14 14" fill="none" stroke="#fff" stroke-width="1.3"><circle cx="7" cy="4.5" r="3"/><path d="M1.5 13c.5-3 3-4.5 5.5-4.5s5 1.5 5.5 4.5"/></svg>
    <svg width="14" height="14" viewBox="0 0 14 14" fill="none" stroke="#fff" stroke-width="1.3"><path d="M7 12.5 1.8 7.2A3 3 0 0 1 7 3a3 3 0 0 1 5.2 4.2z"/></svg>
  </div>
</div>

<!-- header -->
<div class="abs header">
  <div class="abs logo"><span class="mark"></span><b>Morvena</b></div>
  <div class="abs promo">
    <p>Discount codes for <em>new email</em> subscribers</p>
    <small>Fresh styles weekly, join our list for exclusive member offers</small>
  </div>
  <div class="abs search">SEARCH...
    <svg width="12" height="12" viewBox="0 0 12 12" fill="none" stroke="#999" stroke-width="1.3"><circle cx="5" cy="5" r="4"/><path d="M8 8l3.5 3.5"/></svg>
  </div>
  <div class="abs cart">
    <svg width="28" height="28" viewBox="0 0 28 28" fill="none" stroke="#333" stroke-width="1.5"><path d="M3 9h22l-2 17H5z"/><path d="M9 9V6a5 5 0 0 1 10 0v3"/></svg>
    <span class="badge">2</span>
  </div>
</div>

<!-- navigation -->
<nav class="abs nav">
  <ul>
    <li class="active">HOME</li><li>NEW ARRIVALS</li><li>PRE-ORDER</li><li>MEN COLLECTION<i>⌄</i></li><li>WOMEN COLLECTION<i>⌄</i></li><li>SEASON COLLECTIONS<i>⌄</i></li><li>BAGS</li><li>ACCESSORIES</li>
  </ul>
</nav>

<!-- hero -->
<section class="abs hero">
  <div class="abs photo" role="img" aria-label="Model in a grey blazer holding a silver croc-effect handbag"></div>
  <svg class="abs" style="left:158px;top:254px" width="12" height="20" viewBox="0 0 12 20" fill="none" stroke="#fff" stroke-width="2"><path d="M10 2 2 10l8 8"/></svg>
  <svg class="abs" style="left:1028px;top:254px" width="12" height="20" viewBox="0 0 12 20" fill="none" stroke="#fff" stroke-width="2"><path d="m2 2 8 8-8 8"/></svg>
  <div class="abs copy">
    <div class="kick">Hurry Up!</div>
    <h2>DISCOUNT DEALS</h2>
    <h3>ON WOMEN BAGS</h3>
    <div class="sub">This Week Only!</div>
  </div>
  <span class="btn">SHOP NOW</span>
  <div class="abs dots"><span></span><span class="on"></span><span></span></div>
</section>

<!-- latest products -->
<h2 class="abs title" style="top:785px">LATEST PRODUCTS</h2>
<svg class="arrow" style="left:148px;top:974px" width="24" height="16" viewBox="0 0 24 16" fill="none" stroke="#333" stroke-width="1.5"><path d="M23 8H2M8 2 2 8l6 6"/></svg>
<svg class="arrow" style="left:1026px;top:974px" width="24" height="16" viewBox="0 0 24 16" fill="none" stroke="#333" stroke-width="1.5"><path d="M1 8h21M16 2l6 6-6 6"/></svg>

<div class="abs active-card" style="left:372px;top:856px;width:232px;height:322px"></div>

<div class="abs card" style="left:161px;top:869px">
  <div class="img"><div class="shape" role="img" aria-label="Brown leather crossbody bag" style="width:130px;height:90px;background:radial-gradient(ellipse,#8a6a4a 40%,#fff 72%)"></div></div>
  <div class="stars">☆☆☆☆☆</div><div class="name">Product Name</div><div class="price">$150.00</div>
</div>
<div class="abs card" style="left:386px;top:869px">
  <div class="img"><div class="shape" role="img" aria-label="Tan leather tote handbag" style="width:130px;height:130px;background:radial-gradient(ellipse,#8e4a2a 40%,#fff 72%)"></div>
    <div class="tools-v">
      <span><svg width="11" height="11" viewBox="0 0 12 12" fill="var(--gold)"><path d="M1 2h2l1.5 6h6l1-4.5H4"/><circle cx="5" cy="10.5" r="1"/><circle cx="10" cy="10.5" r="1"/></svg></span>
      <span><svg width="11" height="11" viewBox="0 0 14 14" fill="var(--gold)"><path d="M7 12.5 1.8 7.2A3 3 0 0 1 7 3a3 3 0 0 1 5.2 4.2z"/></svg></span>
      <span><svg width="12" height="10" viewBox="0 0 14 10" fill="var(--gold)"><path d="M7 1C3.5 1 1 5 1 5s2.5 4 6 4 6-4 6-4-2.5-4-6-4z"/><circle cx="7" cy="5" r="2" fill="#2b2b2b"/></svg></span>
    </div></div>
  <div class="stars">☆☆☆☆☆</div><div class="name">Product Name</div><div class="price">$150.00</div>
</div>
<div class="abs card" style="left:612px;top:869px">
  <div class="img"><div class="shape" role="img" aria-label="White leather shopper bag" style="width:130px;height:120px;background:radial-gradient(ellipse,#d6d6d6 45%,#fff 72%)"></div><span class="tag">NEW ARRIVAL</span></div>
  <div class="stars">☆☆☆☆☆</div><div class="name">Product Name</div><div class="price">$150.00</div>
</div>
<div class="abs card" style="left:837px;top:869px">
  <div class="img"><div class="shape" role="img" aria-label="Grey leather duffle bag" style="width:130px;height:100px;background:radial-gradient(ellipse,#bdbdbd 45%,#fff 72%)"></div><span class="tag">NEW ARRIVAL</span></div>
  <div class="stars">☆☆☆☆☆</div><div class="name">Product Name</div><div class="price">$150.00</div>
</div>

<div class="abs divider"></div>

<!-- collections -->
<div class="tile" style="left:154px;top:1299px;width:439px;height:411px;background:linear-gradient(90deg,#cfcfcf,#f0efed 50%,#d4d4d4)" role="img" aria-label="Woman in white jacket carrying a black leather bag">
  <div class="panel" style="left:28px;top:129px;width:383px;height:152px;padding-top:40px">
    <h4>COLLECTION FOR THE LADIES</h4><span class="btn">SHOP NOW</span>
  </div>
</div>
<div class="tile" style="left:612px;top:1299px;width:200px;height:195px;background:linear-gradient(180deg,#dcdcdc 45%,#555 75%,#3a3a3a)" role="img" aria-label="Black leather handbag">
  <div style="position:absolute;left:0;top:30px;width:200px;text-align:center"><h4>HAND BAGS</h4><small>Shop Women Bag</small></div>
</div>
<div class="tile" style="left:837px;top:1299px;width:202px;height:195px;background:linear-gradient(180deg,#9a9a9a,#d8d8d8 55%,#e2e2e2 60%)" role="img" aria-label="Black leather sneakers on a model">
  <div style="position:absolute;left:0;top:132px;width:202px;text-align:center"><h4>WOMAN SHOES</h4><small>Click Here To Shop Now</small></div>
</div>
<div class="tile" style="left:612px;top:1517px;width:427px;height:193px;background:linear-gradient(90deg,#b8957a,#5a5a5a 30%,#d8d8d8 65%,#eaeaea)" role="img" aria-label="Nude and black leather heels on marble">
  <div class="panel" style="left:38px;top:34px;width:352px;height:87px;padding-top:20px">
    <h4>FIND OUT LATEST COLLECTIONS</h4>
  </div>
  <span class="btn" style="position:absolute;left:146px;top:92px;width:114px;height:39px;line-height:39px">SHOP NOW</span>
</div>

<!-- featured products -->
<h2 class="abs title" style="top:1826px">FEATURED PRODUCTS</h2>
<svg class="arrow" style="left:148px;top:2015px" width="24" height="16" viewBox="0 0 24 16" fill="none" stroke="#333" stroke-width="1.5"><path d="M23 8H2M8 2 2 8l6 6"/></svg>
<svg class="arrow" style="left:1026px;top:2015px" width="24" height="16" viewBox="0 0 24 16" fill="none" stroke="#333" stroke-width="1.5"><path d="M1 8h21M16 2l6 6-6 6"/></svg>

<div class="abs active-card" style="left:372px;top:1897px;width:232px;height:322px"></div>

<div class="abs card" style="left:161px;top:1910px">
  <div class="img"><div class="shape" role="img" aria-label="Nude leather peep-toe heel" style="width:110px;height:70px;background:radial-gradient(ellipse,#d8b79c 40%,#fff 72%)"></div></div>
  <div class="stars">☆☆☆☆☆</div><div class="name">Product Name</div><div class="price">$150.00</div>
</div>
<div class="abs card" style="left:386px;top:1910px">
  <div class="img"><div class="shape" role="img" aria-label="Beige and black patent pump" style="width:110px;height:90px;background:radial-gradient(ellipse,#7a6a60 40%,#fff 72%)"></div>
    <div class="tools-v">
      <span><svg width="11" height="11" viewBox="0 0 12 12" fill="var(--gold)"><path d="M1 2h2l1.5 6h6l1-4.5H4"/><circle cx="5" cy="10.5" r="1"/><circle cx="10" cy="10.5" r="1"/></svg></span>
      <span><svg width="11" height="11" viewBox="0 0 14 14" fill="var(--gold)"><path d="M7 12.5 1.8 7.2A3 3 0 0 1 7 3a3 3 0 0 1 5.2 4.2z"/></svg></span>
      <span><svg width="12" height="10" viewBox="0 0 14 10" fill="var(--gold)"><path d="M7 1C3.5 1 1 5 1 5s2.5 4 6 4 6-4 6-4-2.5-4-6-4z"/><circle cx="7" cy="5" r="2" fill="#2b2b2b"/></svg></span>
    </div></div>
  <div class="stars">☆☆☆☆☆</div><div class="name">Product Name</div><div class="price">$150.00</div>
</div>
<div class="abs card" style="left:612px;top:1910px">
  <div class="img"><div class="shape" role="img" aria-label="Nude and red ankle-strap heel" style="width:110px;height:90px;background:radial-gradient(ellipse,#c8584a 35%,#fff 72%)"></div></div>
  <div class="stars">☆☆☆☆☆</div><div class="name">Product Name</div><div class="price">$150.00</div>
</div>
<div class="abs card" style="left:837px;top:1910px">
  <div class="img"><div class="shape" role="img" aria-label="Nude slingback heel" style="width:110px;height:80px;background:radial-gradient(ellipse,#d9bba5 40%,#fff 72%)"></div><span class="tag">OUT OF STOCK</span></div>
  <div class="stars">☆☆☆☆☆</div><div class="name">Product Name</div><div class="price">$150.00</div>
</div>
<div class="abs notify">
  <svg width="14" height="14" viewBox="0 0 14 14" fill="none"><rect x=".5" y=".5" width="13" height="13" fill="#fff" stroke="#ddd"/><path d="m3 7 3 3 5-6" stroke="var(--gold)" stroke-width="1.5"/></svg>
  Notify Me When It Gets Back On Stock
</div>

<!-- latest news -->
<h2 class="abs title" style="top:2334px">LATEST NEWS</h2>

<article class="abs news" style="left:161px;top:2418px">
  <div class="img" role="img" aria-label="Woman trying on leather boots in a city square" style="background:linear-gradient(90deg,#2f5a5e,#9a8a78 50%,#c9c2b8)"><span class="date">17 <small>/ feb</small></span></div>
  <div class="meta"><span><b></b>By: Admin</span><span><b></b>2Comments</span><span><b></b>Shoes</span></div>
  <h5>Comfortable shoes enhances on your confidence</h5>
  <p>Soft leather insoles and cushioned heels keep you steady all day, so every step feels natural and assured on any surface.</p>
  <span class="btn">READ ARTICLE</span>
</article>
<article class="abs news" style="left:462px;top:2418px">
  <div class="img" role="img" aria-label="Woman in red coat looking at her phone" style="background:linear-gradient(90deg,#d8d8d8,#d63a3a 45%,#c9c9c9)"><span class="date">20 <small>/ feb</small></span></div>
  <div class="meta"><span><b></b>By: Admin</span><span><b></b>2Comments</span><span><b></b>Shoes</span></div>
  <h5>Comfortable shoes enhances on your confidence</h5>
  <p>Soft leather insoles and cushioned heels keep you steady all day, so every step feels natural and assured on any surface.</p>
  <span class="btn">READ ARTICLE</span>
</article>

<div class="abs nfy">
  <h4>NEWS FOR YOU</h4>
  <small>Just In Now</small>
  <div class="pn"><span>← &nbsp;PREV</span><span class="next">NEXT &nbsp;→</span></div>
</div>

<!-- testimonial -->
<div class="abs avatar" role="img" aria-label="Customer portrait"></div>
<div class="abs quote-mark">“</div>
<svg class="abs" style="left:160px;top:3012px" width="10" height="14" viewBox="0 0 10 14"><path d="M9 0v14L0 7z" fill="#111"/></svg>
<svg class="abs" style="left:1030px;top:3012px" width="10" height="14" viewBox="0 0 10 14"><path d="M1 0v14l9-7z" fill="#111"/></svg>
<p class="abs quote">Distillery retro blue bottle everyday carry chia cronut mixtape mlkshk. Four dollar toast sustainable offal tbh. Subway tile tattooed jianbing, drinking vinegar slow-carb echo park plaid meditation keytar retro lyft mixtape. Pug cred kale chips unicorn mlkshk. Mixtape sustainable subway tile helvetica copper mug. Banh mi activated charcoal direct trade, meh cardigan chambray heirloom lo-fi church-key</p>
<div class="abs qline"></div>
<div class="abs author">- Leon Varesco &nbsp;<small>- Satisfied Costumer</small></div>

<!-- footer -->
<footer class="abs footer">
  <div class="fcol" style="left:43px">
    <h6>INFORMATION</h6>
    <ul><li>About Us</li><li>Delivery Information</li><li>Privacy Policy</li><li>Terms &amp; Conditions</li><li>Payments</li><li>Contact Us</li></ul>
  </div>
  <div class="vsep" style="left:237px"></div>
  <div class="fcol news-l">
    <h6>NEWSLETTER</h6>
    <p>Subscribe here to get notified about all the fresh baked<br>updates. Discount codes for new email subscribers</p>
    <div class="subs">Enter Your Email Address
      <span><svg width="16" height="16" viewBox="0 0 16 16"><path d="M15 1 1 7l5 2 2 6z" fill="var(--gold)"/></svg></span>
    </div>
  </div>
  <div class="vsep" style="left:638px"></div>
  <div class="fcol contact" style="left:684px">
    <h6>CONTACT US</h6>
    <p>Lorem custom Site ipsum<br>Boltacusta avenue ap ,600<br>Mesa,California</p>
    <p>12-3456-7890 (+91)<br><br>12-3456-7890 (+91)</p>
    <p>info@example.com</p>
  </div>
</footer>

<div class="abs bottom">
  <div class="pay">Pay Via: <b>Marquo</b><b>Veyra</b><b>CoinLane</b></div>
  <div>Powered By <b>Morvena</b> © 2020</div>
  <div class="find">Find Us At: <span class="dot"></span><span class="dot" style="background:var(--gold)"></span><span class="dot"></span></div>
</div>

<nav class="abs bnav">
  <ul><li>HOME</li><li>NEW ARRIVALS</li><li>PRE-ORDER</li><li>MEN COLLECTION</li><li>WOMEN COLLECTION</li><li>SEASON COLLECTIONS</li><li>BAGS</li><li>ACCESSORIES</li></ul>
</nav>

</body>
</html>
```